Quillmark Select

Letter Head, Envelope, Business Cards, Social Media Banner (FB/Twitter), Social Media Icon, Social Media Announcement Template...

We are a Softball Team/Organization

Target Market(s)

High School Student-Athletes (softball players) and their parents

Font styles to use
Serif

Requirements
Must have
• Logo & Colors
Must POP and say WOW
Common theme amongst all designs

```html
<!DOCTYPE html>
<html lang="en">
<head>
<meta charset="utf-8">
<title>Quillmark Select — Stationery</title>
<link href="https://fonts.googleapis.com/css2?family=Montserrat:wght@400;700&family=Barlow+Semi+Condensed:wght@400&family=Lato:wght@400;700&display=swap" rel="stylesheet">
<style>
  :root{
    --navy:#1e3763;
    --backdrop:#d8e4ef;
    --paper:#ffffff;
    --ink:#555a60;
    --ink-dark:#4a4d52;
    --rule:#9aa3ad;
    --shadow:0 3px 6px rgba(40,60,90,.28);
  }
  *{margin:0;padding:0;box-sizing:border-box}
  html,body{width:1200px;height:832px;overflow:hidden}
  body{background:var(--backdrop);position:relative;font-family:"Lato",sans-serif;color:var(--ink)}

  .sheet{position:absolute;background:var(--paper);box-shadow:var(--shadow)}
  .top-band{position:absolute;left:0;top:0;right:0;background:var(--navy)}

  /* brand name block */
  .brand{position:absolute;display:flex;align-items:center;gap:.35em;font-family:"Montserrat",sans-serif;font-weight:700;color:var(--navy);text-transform:uppercase;letter-spacing:.06em;line-height:1.05}
  .brand .mark{width:1.6em;height:1.6em;background:currentColor;flex:none}
  .brand.on-navy{color:#fff}

  /* letterhead */
  .letterhead{left:116px;top:112px;width:431px;height:608px}
  .letterhead .top-band{height:6px}
  .letterhead .brand{left:41px;top:45px;font-size:13px}
  .contact{position:absolute;left:311px;top:36px;font-family:"Lato",sans-serif;font-size:7.8px;line-height:10.5px;color:var(--ink)}
  .contact .address{margin-bottom:3px}
  .contact li{list-style:none;display:flex;align-items:center;gap:6px}
  .contact svg{width:7px;height:7px;fill:var(--navy)}
  .date{position:absolute;left:42px;top:208px;font-family:"Montserrat",sans-serif;font-size:9.4px;color:var(--ink)}
  .recipient{position:absolute;left:41px;top:224px;font-family:"Montserrat",sans-serif;font-weight:700;font-size:15.2px;color:var(--ink-dark)}
  .role{position:absolute;left:41px;top:245px;font-family:"Montserrat",sans-serif;font-size:9.4px;color:var(--ink)}
  .letter-body{position:absolute;left:41px;top:283px;width:350px;font-family:"Barlow Semi Condensed",sans-serif;font-size:8.2px;line-height:15px;color:var(--ink-dark);text-align:justify}
  .letter-body p{margin-bottom:15px}
  .signoff{position:absolute;left:41px;top:452px;font-family:"Barlow Semi Condensed",sans-serif;font-size:9.6px;color:var(--ink-dark)}
  .signature{position:absolute;left:41px;top:474px;width:46px;height:30px;background:linear-gradient(135deg,#e6ebf2,#d2dbe8)}

  /* business cards */
  .card{width:182px;height:104px}
  .card-front{left:636px;top:112px}
  .card-front .top-band{height:3px}
  .card-front .brand{right:11px;top:16px;font-size:7.5px;text-align:right}
  .card-name{position:absolute;left:10px;top:55px;font-family:"Montserrat",sans-serif;font-weight:700;font-size:8.4px;color:var(--navy)}
  .card-title{position:absolute;left:10px;top:65px;font-size:4.6px;color:var(--ink)}
  .card-rule{position:absolute;left:10px;right:11px;top:74px;height:.6px;background:var(--rule)}
  .card-contact{position:absolute;left:10px;top:79px;font-size:4.6px;line-height:6.8px;color:var(--ink)}
  .card-contact li{list-style:none;display:flex;align-items:center;gap:3px}
  .card-contact svg{width:4px;height:4px;fill:var(--navy)}
  .card-address{position:absolute;right:11px;top:84px;font-size:4.6px;line-height:6.8px;text-align:right;color:var(--ink)}
  .card-back{left:905px;top:111px;background:var(--navy)}
  .card-back .brand{left:44px;top:42px;font-size:10px}

  /* envelopes */
  .envelope{width:451px;height:226px}
  .envelope-back{left:636px;top:248px}
  .envelope-back .flap{position:absolute;left:0;top:0;width:451px;height:66px}
  .envelope-back .brand{left:0;right:0;top:23px;justify-content:center;font-size:9.5px}
  .envelope-front{left:636px;top:494px}
  .envelope-front .top-band{height:6px}
  .envelope-front .brand{left:44px;top:44px;font-size:14px}
  .return-address{position:absolute;left:44px;top:182px;padding-left:8px;border-left:1.3px solid var(--navy);font-family:"Montserrat",sans-serif;font-size:9.4px;line-height:12px;color:var(--ink)}
</style>
</head>
<body>

<svg width="0" height="0" style="position:absolute">
  <symbol id="icon-phone" viewBox="0 0 24 24"><path d="M6.6 10.8a15 15 0 0 0 6.6 6.6l2.2-2.2a1 1 0 0 1 1-.25 11.4 11.4 0 0 0 3.6.57 1 1 0 0 1 1 1V20a1 1 0 0 1-1 1A17 17 0 0 1 3 4a1 1 0 0 1 1-1h3.5a1 1 0 0 1 1 1c0 1.25.2 2.45.57 3.6a1 1 0 0 1-.25 1z"/></symbol>
  <symbol id="icon-mail" viewBox="0 0 24 24"><path d="M2 5h20v14H2zm2 2v.5l8 5 8-5V7zm0 2.8V17h16V9.8l-8 5z"/></symbol>
  <symbol id="icon-web" viewBox="0 0 24 24"><path d="M12 2a10 10 0 1 0 0 20 10 10 0 0 0 0-20zm7.9 9h-3.4a15 15 0 0 0-1.3-6A8 8 0 0 1 19.9 11zM12 4.1c.9 1.3 2 3.6 2.4 6.9H9.6C10 7.7 11.1 5.4 12 4.1zM8.8 5a15 15 0 0 0-1.3 6H4.1A8 8 0 0 1 8.8 5zM4.1 13h3.4a15 15 0 0 0 1.3 6A8 8 0 0 1 4.1 13zm7.9 6.9c-.9-1.3-2-3.6-2.4-6.9h4.8c-.4 3.3-1.5 5.6-2.4 6.9zm3.2-.9a15 15 0 0 0 1.3-6h3.4a8 8 0 0 1-4.7 6z"/></symbol>
</svg>

<!-- Letterhead -->
<section class="sheet letterhead">
  <div class="top-band"></div>
  <div class="brand"><span class="mark"></span><span>Quillmark<br>Select</span></div>
  <div class="contact">
    <div class="address">18u Quillmark Select<br>240 Harbor Field Road</div>
    <ul>
      <li><svg><use href="#icon-phone"/></svg>555-014-2290</li>
      <li><svg><use href="#icon-mail"/></svg>info@quillmarkselect.com</li>
      <li><svg><use href="#icon-web"/></svg>www.quillmarkselect.com</li>
    </ul>
  </div>
  <p class="date">01 December, 2021</p>
  <h1 class="recipient">DANA WHITFIELD</h1>
  <p class="role">Cheif Executive Officer</p>
  <div class="letter-body">
    <p>Contrary to popular belief, Lorem Ipsum is not simply random text. It has roots in a piece of classical Latin literature from 45 BC, making it over 2000 years old. Arthur Pell, a Latin professor at Linwood College in Ohio, looked up one of the more obscure Latin words, consectetur.</p>
    <p>Lorem Ipsum comes from sections 1.10.32 and 1.10.33 of "de Finibus Bonorum et Malorum" (The Extremes of Good and Evil) by Aurelian Teno, written in 45 BC. This book is a treatise on the theory of ethics, very popular during the Renaissance. The first line of Lorem Ipsum.</p>
    <p>The standard chunk of Lorem Ipsum used since the 1500s is reproduced below for those interested.</p>
  </div>
  <p class="signoff">Best Regards</p>
  <div class="signature" role="img" aria-label="Handwritten signature"></div>
</section>

<!-- Business card front -->
<section class="sheet card card-front">
  <div class="top-band"></div>
  <div class="brand"><span class="mark"></span><span>Quillmark<br>Select</span></div>
  <h2 class="card-name">LENA MARSH</h2>
  <p class="card-title">Founder &amp; CEO</p>
  <div class="card-rule"></div>
  <ul class="card-contact">
    <li><svg><use href="#icon-phone"/></svg>(555) 013-7740</li>
    <li><svg><use href="#icon-mail"/></svg>info@quillmarkselect.com</li>
    <li><svg><use href="#icon-web"/></svg>www.quillmarkselect.com</li>
  </ul>
  <p class="card-address">18u Quillmark Select<br>240 Harbor Field Road</p>
</section>

<!-- Business card back -->
<section class="sheet card card-back">
  <div class="brand on-navy"><span class="mark"></span><span>Quillmark<br>Select</span></div>
</section>

<!-- Envelope back -->
<section class="sheet envelope envelope-back">
  <svg class="flap" viewBox="0 0 451 66" preserveAspectRatio="none">
    <path d="M0 0H451L446 44Q444 66 420 66H30Q6 66 5 44Z" fill="var(--navy)"/>
  </svg>
  <div class="brand on-navy"><span class="mark"></span><span>Quillmark<br>Select</span></div>
</section>

<!-- Envelope front -->
<section class="sheet envelope envelope-front">
  <div class="top-band"></div>
  <div class="brand"><span class="mark"></span><span>Quillmark<br>Select</span></div>
  <p class="return-address">18u Quillmark Select<br>240 Harbor Field Road</p>
</section>

</body>
</html>
```